LoomBay App Design

The attached document, [LoomBay - Design & Requirements Document - v1.2], outlines the full design and functional requirements for the LoomBay App. The key sections include:
• Company overview: Mission and vision statements
• High-level application overview
• App design guidelines
• App functional requirements
• Navigation information
To expedite app development, we are planning to use a Multi-Purpose PWA Mobile App Template. This template offers pre-built UI elements and layouts that are flexible and responsive, allowing for quicker development while maintaining a modern design.
Artisan Hive Requirements:
We require designs for 11 app pages and 1 pop-up, as outlined in sections 3.13 and section 4 of the document. These designs should be delivered in Adobe format (as a minimum), ready to be handed over to our developers who will build the app using the template and corresponding code base.
Important Notes:
1. Leverage the Multi-Purpose PWA Mobile App Template: The designs must make use of the components and features available within the template. You can explore the template using the following link to view the pages, features, and styles:
o Template link: Venra: Multi-Purpose PWA Mobile App Template
2. Sample screens for Visual Reference: To aid in visualizing the app's navigation, please refer to the sample screens. This serves as a high-level guide to demonstrate the user flow but is not a literal requirement for the design.
o Note:
 Not all features and pages from the requirements document are represented in these screen samples
 The flow is provided purely to showcase the navigational paths within the app.

Deliverables:
The designs should align with the template's style, features, and UI components, with clear attention to how each page will function within the LoomBay app. The final designs are expected to be in Adobe format for smooth developer handoff.
To confirm, we are looking to see how best to utilise the template design style etc for the APP’s final design, whilst incorporating all the requirements of the APP from the requirements document.

Target Market(s)

Young shopping demographic

Industry/Entity Type

Online Shopping

Requirements
Must have
• All the required pages designed
Nice to have
• See requirements document

```html
<!DOCTYPE html>
<html lang="en">
<head>
<meta charset="utf-8">
<title>LoomBay App Screens</title>
<link rel="stylesheet" href="https://fonts.googleapis.com/css2?family=Lato:ital,wght@0,400;0,700;0,900;1,400&family=Ubuntu:wght@400;500;700&display=swap">
<style>
:root{
  --orange:#e8711e;
  --orange-soft:#f08c3e;
  --ink:#111111;
  --text:#3a3a3a;
  --muted:#9b9b9b;
  --line:#dcdcdc;
  --canvas:#7f7f7f;
  --field:#f4f4f5;
  --green:#2fc937;
  --disabled:#c6c6c6;
  --slate:#3d4a56;
}
*{box-sizing:border-box;margin:0;padding:0}
html,body{width:989px;height:1200px;overflow:hidden;background:var(--canvas)}
body{font-family:"Lato",sans-serif;color:var(--text)}
.board{position:absolute;left:0;top:0;width:1736px;height:2107px;transform:scale(.5697);transform-origin:0 0}
.screen{position:absolute;width:273px;background:#fff;overflow:hidden}
.a{position:absolute}
.center{left:0;right:0;text-align:center}
.brand{font-family:"Ubuntu",sans-serif;font-weight:700;font-size:18px;color:var(--ink)}
.topbar{position:absolute;left:0;top:0;width:273px;height:44px;background:#000;color:#fff}
.topbar .brand{color:#fff;position:absolute;left:0;right:0;top:12px;text-align:center}
.topbar .back{position:absolute;left:18px;top:15px;width:14px;height:14px}
.topbar .me{position:absolute;left:234px;top:12px;width:18px;height:18px}
.title{font-family:"Ubuntu",sans-serif;font-weight:500;font-size:13.5px;letter-spacing:.4px;color:#444}
.para{font-size:8.6px;line-height:12.4px;color:#555;padding:0 30px}
.field{position:absolute;height:32px;border:1.5px solid var(--line);border-radius:17px;font-size:11px;color:var(--muted);padding:0 13px;display:flex;align-items:center}
.btn{position:absolute;height:32px;border-radius:17px;background:var(--orange);color:#fff;font-size:11px;font-weight:900;display:flex;align-items:center;justify-content:center;gap:6px;letter-spacing:.2px}
.btn-outline{background:#fff;border:1.5px solid var(--orange);color:var(--orange)}
.small{font-size:8.6px;color:#555}
.links{font-size:8.6px;color:#555;display:flex;justify-content:center;gap:9px}
.links i{width:1px;height:12px;background:#777}
.social{position:absolute;left:51px;width:171px;height:46px;border:1.5px solid var(--orange);border-radius:3px;display:flex;align-items:center;gap:30px;padding-left:22px;font-family:"Ubuntu",sans-serif;font-size:10.5px;line-height:12px;color:#333;letter-spacing:.3px}
.social .dot{width:20px;height:20px;border-radius:50%;background:#444}
.label{position:absolute;left:21px;font-size:8.3px;font-weight:900;color:#444;letter-spacing:.2px}
.value{position:absolute;left:21px;font-size:11px;color:var(--muted)}
.radios{position:absolute;left:21px;display:flex;gap:14px;font-size:11px;color:var(--muted)}
.radios span{display:flex;align-items:center;gap:6px}
.radios b{width:10px;height:10px;border:1.5px solid #888;border-radius:50%;display:inline-block}
.radios b.on{border-color:var(--orange);background:radial-gradient(var(--orange) 40%,#fff 45%)}
.radios b.on-dark{border-color:#666;background:radial-gradient(#777 40%,#fff 45%)}
.check{width:16px;height:16px;border:1.5px solid #555;border-radius:3px;display:inline-block}
.photo{background:linear-gradient(165deg,#d4d6d7 0%,#a7abae 35%,#6d7073 55%,#c9cbcc 80%,#e0e1e1 100%)}
.tile{position:absolute;top:129px;width:104px;height:108px;background:var(--field);border-radius:10px;display:flex;flex-direction:column;align-items:center;justify-content:center;gap:10px;font-size:8.6px;color:var(--orange)}
.tile svg{width:26px;height:26px}
.pill{position:absolute;background:#000;color:#fff;border-radius:14px;font-size:8.4px;line-height:9px;display:flex;align-items:center;padding:0 14px;white-space:nowrap}
.tabbar{position:absolute;left:0;bottom:0;width:273px;height:47px;background:#fff;box-shadow:0 -2px 4px rgba(0,0,0,.08)}
.tab{position:absolute;top:9px;transform:translateX(-50%);display:flex;flex-direction:column;align-items:center;gap:3px;font-size:8.4px;color:#999}
.tab svg{width:14px;height:14px}
.tab.on{color:var(--orange)}
.avatar{position:absolute;width:32px;height:32px;border-radius:50%;background:#000;border:2px solid #fff;display:flex;align-items:center;justify-content:center}
.avatar svg{width:20px;height:20px}
.box{position:absolute;border:1.5px solid #222;border-radius:6px;font-size:8.6px;line-height:16.6px;color:#666;padding:10px 18px 0 26px}
.bubble{position:absolute;background:#000;color:#fff;border-radius:8px;font-size:8.6px;display:flex;align-items:center;padding-left:17px}
.handle{position:absolute;left:65px;width:144px;height:3px;background:#888;border-radius:2px}
.msg{position:absolute;left:16px;width:240px;height:34px;border:1.5px solid var(--line);border-radius:17px;font-size:11px;color:var(--muted);display:flex;align-items:center;padding:0 14px;justify-content:space-between}
.dashed{position:absolute;border:1px dashed #fff;border-radius:4px}
.tag{position:absolute;background:#fff;border-radius:3px;font-size:8.4px;color:#222;padding:3px 6px}
.badge{position:absolute;left:0;width:76px;height:30px;background:var(--green);color:#fff;font-size:11px;font-weight:900;display:flex;align-items:center;gap:6px;padding-left:14px;clip-path:polygon(0 0,88% 0,100% 50%,88% 100%,0 100%)}
.badge i,.mini-badge i{width:12px;height:12px;border-radius:50%;background:#fff;display:inline-block}
.sizes{position:absolute;left:14px;display:flex;gap:7px}
.sizes span{width:35px;height:16px;border:1px solid var(--line);border-radius:9px;font-size:7.5px;color:#888;display:flex;align-items:center;justify-content:center}
.swatch{position:absolute;width:18px;height:18px;border-radius:50%}
.ship{position:absolute;left:164px;width:96px;height:16px;background:var(--slate);border-radius:9px;color:#fff;font-size:8px;display:flex;align-items:center;justify-content:center;gap:4px}
.tabs{position:absolute;left:14px;display:flex;gap:14px;font-size:8.6px;color:#bbb}
.tabs .on{color:var(--orange);border-bottom:1px solid var(--orange);padding-bottom:2px}
.lorem{position:absolute;left:21px;width:240px;font-size:8.6px;line-height:16.7px;color:#999}
.price-old{font-size:10px;color:#888;text-decoration:line-through}
.price{font-family:"Ubuntu",sans-serif;font-size:18.5px;font-weight:700;color:#111}
.pname{font-family:"Ubuntu",sans-serif;font-size:13.5px;font-weight:500;color:#222;letter-spacing:.3px}
.send{position:absolute;width:30px;height:30px;border-radius:50%;background:var(--orange);display:flex;align-items:center;justify-content:center}
.send svg{width:15px;height:15px}
.cta{position:absolute;top:640px;width:137px;height:50px;font-size:11px;font-weight:900;color:#fff;display:flex;align-items:center;justify-content:center;letter-spacing:.2px}
.card{position:absolute;background:#fff;border-radius:8px;box-shadow:0 1px 5px rgba(0,0,0,.18);overflow:hidden}
.mini-badge{position:absolute;left:0;width:48px;height:14px;background:var(--green);color:#fff;font-size:6px;font-weight:900;display:flex;align-items:center;gap:3px;padding-left:4px;clip-path:polygon(0 0,86% 0,100% 50%,86% 100%,0 100%)}
.mini-badge i{width:7px;height:7px}
.cart-card{position:absolute;left:18px;width:237px;border:1px solid #ccc;border-radius:6px;background:#fff;overflow:hidden}
.cart-head{height:44px;font-family:"Ubuntu",sans-serif;font-size:11.5px;color:#333;display:flex;align-items:center;padding-left:16px;box-shadow:0 2px 3px rgba(0,0,0,.12)}
.item-thumb{position:absolute;left:7px;width:45px;height:45px;border-radius:50%}
.item-name{position:absolute;left:62px;font-size:9.2px;font-weight:900;color:#222}
.item-meta{position:absolute;left:62px;font-size:6.3px;line-height:8px;font-style:italic;color:#777}
.remove{position:absolute;left:217px;font-size:11px;color:var(--orange);font-weight:700}
.stepper{position:absolute;left:62px;width:67px;height:20px;display:flex;align-items:center;justify-content:space-between}
.stepper b{width:18px;height:20px;background:#000;color:#fff;font-size:11px;display:flex;align-items:center;justify-content:center;border-radius:10px}
.stepper span{font-size:7px;color:#333}
.item-price{position:absolute;right:10px;font-size:10px;font-weight:900;color:#222}
.rule{position:absolute;left:0;width:237px;height:1px;background:#ccc}
.cal{position:absolute;width:11px;height:11px}
</style>
</head>
<body>
<svg width="0" height="0" style="position:absolute" aria-hidden="true">
  <defs>
    <symbol id="i-back" viewBox="0 0 16 16"><path d="M10.5 2.5 5 8l5.5 5.5" fill="none" stroke="currentColor" stroke-width="2.2"/></symbol>
    <symbol id="i-user" viewBox="0 0 20 20"><circle cx="10" cy="10" r="8.5" fill="none" stroke="currentColor" stroke-width="2"/><circle cx="10" cy="8" r="3" fill="currentColor"/><path d="M4.6 15.6c1.4-2.2 3.2-3.2 5.4-3.2s4 1 5.4 3.2" fill="currentColor"/></symbol>
    <symbol id="i-search" viewBox="0 0 16 16"><circle cx="6.8" cy="6.8" r="4.8" fill="none" stroke="currentColor" stroke-width="1.8"/><path d="m10.3 10.3 4 4" stroke="currentColor" stroke-width="1.8"/></symbol>
    <symbol id="i-spark" viewBox="0 0 16 16"><path d="M7 2 8.3 6.7 13 8 8.3 9.3 7 14 5.7 9.3 1 8l4.7-1.3z" fill="currentColor"/><path d="M13 1l.6 1.7L15 3.3l-1.4.6L13 5.5l-.6-1.6L11 3.3l1.4-.6z" fill="currentColor"/></symbol>
    <symbol id="i-cart" viewBox="0 0 16 16"><path d="M1 2h2.4l1.8 8h7.6l1.6-6H4.3" fill="none" stroke="currentColor" stroke-width="1.6"/><rect x="4.4" y="4.6" width="9.2" height="4.2" fill="currentColor"/><circle cx="6" cy="13" r="1.3" fill="currentColor"/><circle cx="12" cy="13" r="1.3" fill="currentColor"/></symbol>
    <symbol id="i-gallery" viewBox="0 0 26 26"><rect x="6" y="2" width="18" height="17" rx="1.5" fill="none" stroke="currentColor" stroke-width="2"/><path d="M2 7v17h17" fill="none" stroke="currentColor" stroke-width="2"/><path d="m8 16 5-5 3 3 2-2 4 4" fill="none" stroke="currentColor" stroke-width="1.8"/><circle cx="18" cy="7" r="1.6" fill="currentColor"/></symbol>
    <symbol id="i-camera" viewBox="0 0 26 26"><path d="M3 8h5l2-3h6l2 3h5v14H3z" fill="currentColor"/><circle cx="13" cy="14.5" r="5" fill="#fff"/><path d="M13 12v5M10.5 14.5h5" stroke="currentColor" stroke-width="1.8"/></symbol>
    <symbol id="i-lens" viewBox="0 0 20 20"><circle cx="9" cy="9" r="5.5" fill="none" stroke="#fff" stroke-width="2.4"/><path d="m13 13 4 4" stroke="#fff" stroke-width="2.6"/></symbol>
    <symbol id="i-person" viewBox="0 0 20 20"><circle cx="10" cy="10" r="9" fill="#fff"/><circle cx="10" cy="7.5" r="3.2" fill="#000"/><path d="M4.5 16c1.2-2.7 3.1-4 5.5-4s4.3 1.3 5.5 4z" fill="#000"/></symbol>
    <symbol id="i-send" viewBox="0 0 12 12"><path d="M2 2l9 4-9 4 1.5-4z" fill="currentColor"/></symbol>
    <symbol id="i-arrow" viewBox="0 0 16 16"><path d="M2.5 8h10M8.5 3.5 13 8l-4.5 4.5" fill="none" stroke="#fff" stroke-width="2.2"/></symbol>
    <symbol id="i-cal" viewBox="0 0 12 12"><rect x="1" y="2" width="10" height="9" fill="none" stroke="#bbb" stroke-width="1"/><path d="M1 4.5h10M3 6.5h6M3 8.5h6" stroke="#bbb" stroke-width=".8"/></symbol>
    <symbol id="i-pencil" viewBox="0 0 12 12"><path d="M2 10l1-3 5-5 2 2-5 5z" fill="none" stroke="#fff" stroke-width="1.1"/></symbol>
    <symbol id="i-logout" viewBox="0 0 12 12"><path d="M5 2H2v8h3M5 6h6M8.5 3.5 11 6 8.5 8.5" fill="none" stroke="#fff" stroke-width="1.3"/></symbol>
    <symbol id="i-return" viewBox="0 0 14 14"><path d="M6 2 1.5 6 6 10V7.5c3.5 0 5.5 1 6.5 4 0-4-2-7-6.5-7.5z" fill="#fff"/></symbol>
    <symbol id="i-truck" viewBox="0 0 12 10"><path d="M1 2h6v5H1zM7 4h2.5L11 6v1H7z" fill="none" stroke="#fff" stroke-width=".9"/><circle cx="3" cy="8" r="1" fill="#fff"/><circle cx="9" cy="8" r="1" fill="#fff"/></symbol>
    <symbol id="i-spinner" viewBox="0 0 12 12"><circle cx="6" cy="6" r="4.5" fill="none" stroke="#ddd" stroke-width="1.5"/><path d="M6 1.5A4.5 4.5 0 0 1 10.5 6" fill="none" stroke="#333" stroke-width="1.5"/></symbol>
    <symbol id="i-sort" viewBox="0 0 12 12"><path d="M3.5 10V2M1.5 4l2-2 2 2M8.5 2v8M6.5 8l2 2 2-2" fill="none" stroke="currentColor" stroke-width="1.1"/></symbol>
  </defs>
</svg>

<main class="board">

  <!-- Register -->
  <section class="screen" style="left:14px;top:14px;height:591px">
    <div class="a center brand" style="top:21px">LoomBay</div>
    <h2 class="a center title" style="top:71px">REGISTER</h2>
    <div class="field" style="left:41px;width:192px;top:102px">First Name</div>
    <div class="field" style="left:41px;width:192px;top:147px">Last Name</div>
    <div class="field" style="left:41px;width:192px;top:191px">Email</div>
    <div class="field" style="left:41px;width:192px;top:236px">Password</div>
    <div class="field" style="left:41px;width:192px;top:280px">Confirm Password</div>
    <div class="btn" style="left:76px;width:121px;top:346px">REGISTER</div>
    <p class="a center small" style="top:389px">Already Registered? Login</p>
    <div class="social" style="top:439px"><span class="dot"></span><span>Register with<br>Nimbus</span></div>
    <div class="social" style="top:494px"><span class="dot"></span><span>Register with<br>Orchard</span></div>
  </section>

  <!-- Sign-in -->
  <section class="screen" style="left:301px;top:14px;height:591px">
    <div class="a center brand" style="top:21px">LoomBay</div>
    <h2 class="a center title" style="top:71px">SIGN-IN</h2>
    <div class="field" style="left:41px;width:192px;top:124px">Email</div>
    <div class="field" style="left:41px;width:192px;top:177px">Password</div>
    <div class="a small" style="left:41px;top:222px;display:flex;align-items:center;gap:8px"><span class="check"></span>Remember me</div>
    <div class="a center links" style="top:282px"><span>Forgot Password</span><i></i><span>Register</span></div>
    <div class="btn" style="left:76px;width:121px;top:319px">SIGN-IN</div>
    <div class="btn" style="left:76px;width:121px;top:363px">SIGN-IN AS GUEST</div>
    <div class="social" style="top:435px"><span class="dot"></span><span>Sign in with<br>Nimbus</span></div>
    <div class="social" style="top:491px"><span class="dot"></span><span>Sign in with<br>Orchard</span></div>
  </section>

  <!-- Change password: request -->
  <section class="screen" style="left:588px;top:14px;height:591px">
    <div class="a center brand" style="top:21px">LoomBay</div>
    <h2 class="a center title" style="top:71px">CHANGE PASSWORD</h2>
    <p class="a center para" style="top:96px">Lorem ipsum odor amet, consectetuer adipiscing elit. Suspendisse eleifend rhoncus nulla dictum proin interdum.</p>
    <div class="field" style="left:41px;width:192px;top:161px">Email</div>
    <div class="a center links" style="top:224px"><span>Login</span><i></i><span>Register</span></div>
    <div class="btn" style="left:74px;width:125px;top:258px">RESET PASSWORD</div>
  </section>

  <!-- Change password: sent -->
  <section class="screen" style="left:875px;top:14px;height:591px">
    <div class="a center brand" style="top:21px">LoomBay</div>
    <h2 class="a center title" style="top:71px">CHANGE PASSWORD</h2>
    <p class="a center para" style="top:96px">Lorem ipsum odor amet, consectetuer adipiscing elit. Suspendisse eleifend rhoncus nulla dictum proin interdum.</p>
    <div class="btn" style="left:74px;width:125px;top:161px">BACK TO LOGIN</div>
    <div class="a small" style="left:79px;top:203px;display:flex;align-items:center;gap:6px"><svg width="11" height="11"><use href="#i-spinner"/></svg>Back to login page in 5s</div>
  </section>

  <!-- Change password: new -->
  <section class="screen" style="left:1162px;top:14px;height:591px">
    <div class="a center brand" style="top:21px">LoomBay</div>
    <h2 class="a center title" style="top:71px">CHANGE PASSWORD</h2>
    <p class="a center para" style="top:96px">Lorem ipsum odor amet, consectetuer adipiscing elit. Suspendisse eleifend rhoncus nulla dictum proin interdum.</p>
    <div class="field" style="left:41px;width:192px;top:161px">Password</div>
    <div class="field" style="left:41px;width:192px;top:208px">Confirm Password</div>
    <div class="a center links" style="top:271px"><span>Login</span><i></i><span>Register</span></div>
    <div class="btn" style="left:74px;width:125px;top:305px">RESET PASSWORD</div>
  </section>

  <!-- Edit profile -->
  <section class="screen" style="left:14px;top:620px;height:867px">
    <header class="topbar"><svg class="back"><use href="#i-back"/></svg><div class="brand">LoomBay</div><svg class="me"><use href="#i-user"/></svg></header>
    <h1 class="a pname" style="left:21px;top:63px;font-weight:700">Edit Profile</h1>
    <div class="label" style="top:110px">FIRST NAME</div>
    <div class="field" style="left:29px;width:215px;top:125px">First Name</div>
    <div class="label" style="top:172px">LAST NAME</div>
    <div class="field" style="left:29px;width:215px;top:187px">Last Name</div>
    <div class="label" style="top:235px">DATE OF BIRTH</div>
    <div class="field" style="left:29px;width:215px;top:250px;justify-content:space-between">MM-DD-YYYY*<svg class="cal" style="position:static"><use href="#i-cal"/></svg></div>
    <div class="label" style="top:298px">GENDER</div>
    <div class="radios" style="top:318px"><span><b class="on"></b>Male</span><span><b></b>Female</span><span><b></b>Other</span></div>
    <div class="label" style="top:345px">EMAIL</div>
    <div class="field" style="left:29px;width:215px;top:360px">Email</div>
    <div class="label" style="top:433px">PASSWORD</div>
    <div class="field" style="left:29px;width:215px;top:448px">********</div>
    <div class="field" style="left:29px;width:215px;top:489px">********</div>
    <div class="btn btn-outline" style="left:29px;width:215px;top:531px;height:33px">CONFIRM PASSWORD</div>
    <div class="label" style="top:605px">DELIVERY ADDRESS 1</div>
    <div class="field" style="left:29px;width:215px;top:620px">Address , State, Country, ZIP*</div>
    <div class="a small" style="left:41px;top:659px;display:flex;align-items:center;gap:8px"><span class="check"></span>Set as default delivery address</div>
    <div class="label" style="top:690px">DELIVERY ADDRESS 2</div>
    <div class="field" style="left:29px;width:215px;top:705px">Address , State, Country, ZIP*</div>
    <div class="btn btn-outline" style="left:30px;width:215px;top:746px;height:33px">ADD ADDRESS</div>
    <div class="btn" style="left:92px;width:90px;top:819px;height:33px">SAVE</div>
  </section>

  <!-- Profile -->
  <section class="screen" style="left:301px;top:620px;height:605px">
    <header class="topbar"><svg class="back"><use href="#i-back"/></svg><div class="brand">LoomBay</div><svg class="me"><use href="#i-user"/></svg></header>
    <h1 class="a pname" style="left:21px;top:68px;font-weight:700">Profile</h1>
    <div class="btn" style="left:179px;width:82px;top:64px;height:26px"><svg width="10" height="10"><use href="#i-pencil"/></svg>EDIT</div>
    <div class="label" style="top:119px">FIRST NAME</div>
    <div class="value" style="top:139px">First Name</div>
    <div class="label" style="top:181px">LAST NAME</div>
    <div class="value" style="top:202px">Last Name</div>
    <div class="label" style="top:244px">DATE OF BIRTH</div>
    <div class="value" style="top:264px">MM - DD - YYYY</div>
    <svg class="cal" style="left:215px;top:265px"><use href="#i-cal"/></svg>
    <div class="label" style="top:306px">GENDER</div>
    <div class="radios" style="top:327px"><span><b class="on-dark"></b><i style="font-style:normal;color:#555">Male</i></span><span><b></b>Female</span><span><b></b>Other</span></div>
    <div class="label" style="top:354px">EMAIL</div>
    <div class="value" style="top:374px">user@email.com</div>
    <div class="label" style="top:416px">PASSWORD</div>
    <div class="value" style="top:436px">********</div>
    <div class="label" style="top:479px;left:25px">DELIVERY ADDRESS</div>
    <div class="value" style="top:499px;left:25px">Address, State, Country, ZIP</div>
    <div class="btn" style="left:74px;width:124px;top:557px;height:33px"><svg width="11" height="11"><use href="#i-logout"/></svg>LOGOUT</div>
  </section>

  <!-- Search: start -->
  <section class="screen" style="left:588px;top:620px;height:592px">
    <header class="topbar"><div class="brand">LoomBay</div><svg class="me"><use href="#i-user"/></svg></header>
    <p class="a center para" style="top:78px;padding:0 22px">Provide an image or describe your desired fashion item below, and we'll create a personalized set of recommendations with filters to suit your needs.</p>
    <div class="tile" style="left:25px"><svg><use href="#i-gallery"/></svg>Upload an Image</div>
    <div class="tile" style="left:144px"><svg><use href="#i-camera"/></svg>Take a Photo</div>
    <div class="pill" style="left:17px;top:412px;height:26px">I want a white sleeveless crop top in size small</div>
    <div class="pill" style="left:17px;top:444px;height:35px;white-space:normal;width:213px;border-radius:16px">I am looking for a pink floral 1950's style dress for under $200.</div>
    <div class="a" style="left:18px;top:488px;width:236px;height:32px;background:var(--field);border-radius:16px;font-size:11px;color:#999;display:flex;align-items:center;gap:8px;padding-left:14px"><svg width="10" height="10"><use href="#i-search"/></svg>Describe your fashion item</div>
    <nav class="tabbar">
      <div class="tab on" style="left:52px"><svg><use href="#i-search"/></svg>Search</div>
      <div class="tab" style="left:136px"><svg><use href="#i-spark"/></svg>Recommendations</div>
      <div class="tab" style="left:226px"><svg><use href="#i-cart"/></svg>Cart</div>
    </nav>
  </section>

  <!-- Search: assistant -->
  <section class="screen" style="left:875px;top:620px;height:592px">
    <header class="topbar"><div class="brand">LoomBay</div><svg class="me"><use href="#i-user"/></svg></header>
    <p class="a center para" style="top:78px;padding:0 22px">Provide an image or describe your desired fashion item below, and we'll create a personalized set of recommendations with filters to suit your needs.</p>
    <div class="tile" style="left:25px"><svg><use href="#i-gallery"/></svg>Upload an Image</div>
    <div class="tile" style="left:144px"><svg><use href="#i-camera"/></svg>Take a Photo</div>
    <div class="a" style="left:0;top:250px;width:273px;height:342px;background:#fff;border-radius:18px 18px 0 0;box-shadow:0 -3px 6px rgba(0,0,0,.12)"></div>
    <div class="handle" style="top:261px"></div>
    <div class="box" style="left:38px;top:288px;width:214px;height:78px">Describe below your desired item so we can find the best possible match for you. For example:</div>
    <div class="avatar" style="left:20px;top:309px"><svg><use href="#i-lens"/></svg></div>
    <div class="box" style="left:38px;top:374px;width:214px;height:61px">I want a white sleeveless crop top in size small</div>
    <div class="avatar" style="left:20px;top:387px"><svg><use href="#i-lens"/></svg></div>
    <div class="bubble" style="left:21px;top:457px;width:214px;height:54px">Does this store offer free returns?</div>
    <div class="avatar" style="left:214px;top:468px"><svg><use href="#i-person"/></svg></div>
    <div class="msg" style="top:536px">Message<svg width="9" height="9" style="color:#777"><use href="#i-send"/></svg></div>
  </section>

  <!-- Scanning -->
  <section class="screen" style="left:1162px;top:620px;height:592px">
    <div class="a center" style="top:62px;font-size:11px;color:#222;display:flex;justify-content:center;gap:6px;align-items:center"><svg width="12" height="12"><use href="#i-spinner"/></svg>Scanning Image</div>
    <p class="a center" style="top:91px;font-size:8.2px;line-height:9.5px;color:#888;padding:0 45px">One moment while we analyse the image to identify the clothing item</p>
    <div class="a photo" role="img" aria-label="Fashion photo of a model in a black crop top, white track pants and sneakers being scanned" style="left:27px;top:158px;width:219px;height:372px;border-radius:8px"></div>
    <div class="a" style="left:0;top:584px;width:273px;height:8px;background:#ddd"></div>
    <div class="a" style="left:0;top:584px;width:92px;height:8px;background:#111"></div>
  </section>

  <!-- Completed scan -->
  <section class="screen" style="left:1449px;top:620px;height:592px">
    <div class="a center" style="top:62px;font-size:11px;color:#222">Completed Scan</div>
    <p class="a center" style="top:91px;font-size:8.2px;line-height:9.5px;color:#888;padding:0 50px">Select the item of clothing you wish to search for</p>
    <div class="a photo" role="img" aria-label="Fashion photo of a model with detected top, bottom and shoes regions" style="left:27px;top:158px;width:219px;height:372px;border-radius:8px"></div>
    <div class="dashed" style="left:75px;top:245px;width:99px;height:72px"></div>
    <div class="tag" style="left:139px;top:268px">Top</div>
    <div class="dashed" style="left:79px;top:320px;width:154px;height:80px"></div>
    <div class="tag" style="left:189px;top:330px">Bottom</div>
    <div class="dashed" style="left:79px;top:417px;width:94px;height:65px"></div>
    <div class="tag" style="left:133px;top:421px">Shoes</div>
  </section>

  <!-- Assistant over product -->
  <section class="screen" style="left:301px;top:1239px;height:592px">
    <div class="a photo" role="img" aria-label="Product photo of a model in a black crop top and white track pants" style="left:0;top:0;width:273px;height:190px"></div>
    <svg class="a" style="left:17px;top:26px;width:14px;height:14px;color:#fff"><use href="#i-back"/></svg>
    <div class="a" style="left:0;top:178px;width:273px;height:414px;background:#fff;border-radius:18px 18px 0 0"></div>
    <div class="handle" style="top:190px"></div>
    <div class="bubble" style="left:21px;top:217px;width:215px;height:53px">Does this store offer free returns?</div>
    <div class="avatar" style="left:215px;top:228px"><svg><use href="#i-person"/></svg></div>
    <div class="a" style="right:39px;top:277px;font-size:8.4px;color:#999">20th Sept</div>
    <div class="box" style="left:39px;top:314px;width:213px;height:127px">A flat, $10 free for a prepaid shipping label is payable by the customer during the Returns Portal process. A returns tracking link will be emailed to you when you finalise your return.</div>
    <div class="avatar" style="left:20px;top:361px"><svg><use href="#i-lens"/></svg></div>
    <div class="a" style="left:39px;top:448px;font-size:8.4px;color:#999">20th Sept</div>
    <div class="pill" style="left:17px;top:499px;height:27px;width:123px">What size is the model?</div>
    <div class="pill" style="left:151px;top:499px;height:27px;width:140px">How much is express shipping?</div>
    <div class="msg" style="left:17px;top:536px">Message<svg width="9" height="9" style="color:#777"><use href="#i-send"/></svg></div>
  </section>

  <!-- Product detail -->
  <section class="screen" style="left:588px;top:1227px;height:690px">
    <header class="topbar"><svg class="back"><use href="#i-back"/></svg><div class="brand">Rosa Lane</div><svg class="me"><use href="#i-user"/></svg></header>
    <div class="a photo" role="img" aria-label="Product photo of a model in a black crop top and white track pants" style="left:0;top:44px;width:273px;height:191px"></div>
    <div class="badge" style="top:180px"><i></i>30% OFF</div>
    <div class="a pname" style="left:14px;top:256px">Product Name</div>
    <div class="a" style="right:13px;top:252px;display:flex;align-items:baseline;gap:7px"><span class="price-old">$66.00</span><span class="price">$66.00</span></div>
    <div class="sizes" style="top:287px"><span>S</span><span>M</span><span>L</span><span>XL</span></div>
    <span class="swatch" style="left:14px;top:317px;background:#f06068"></span>
    <span class="swatch" style="left:37px;top:317px;background:#8fd6cc"></span>
    <span class="swatch" style="left:61px;top:317px;background:var(--slate)"></span>
    <div class="ship" style="top:319px"><svg width="11" height="9"><use href="#i-truck"/></svg>Free Shipping</div>
    <div class="tabs" style="top:364px"><span class="on">Description</span><span>Features</span><span>Shipping</span><span>Store Info</span><span>Returns</span></div>
    <p class="lorem" style="top:386px">Lorem ipsum odor amet, consectetuer adipiscing elit. Habitasse neque rhoncus lobortis vehicula hendrerit vel dapibus. Urna cursus facilisis senectus pulvinar neque laoreet venenatis. Ex feugiat felis fermentum laoreet class semper? Orci aliquam nulla mus sapien lorem porttitor venenatis nisi quisque. Eleifend elementum sem efficitur lobortis arcu. Turpis ridiculus vestibulum; faucibus adipiscing morbi at platea dictum.</p>
    <div class="pill" style="left:17px;top:548px;height:27px;width:156px">What size is the model wearing?</div>
    <div class="pill" style="left:185px;top:548px;height:27px;width:120px">How much is express shipping?</div>
    <div class="msg" style="left:17px;top:582px;height:35px"></div>
    <div class="send" style="left:225px;top:585px"><svg><use href="#i-arrow"/></svg></div>
    <div class="cta" style="left:0;background:var(--orange-soft)">ADD TO CART</div>
    <div class="cta" style="left:137px;width:136px;background:var(--orange)">BUY NOW</div>
  </section>

  <!-- Product detail: out of stock -->
  <section class="screen" style="left:875px;top:1227px;height:690px">
    <header class="topbar"><svg class="back"><use href="#i-back"/></svg><div class="brand">Rosa Lane</div><svg class="me"><use href="#i-user"/></svg></header>
    <div class="a photo" role="img" aria-label="Dimmed product photo of a model in a black crop top and white track pants" style="left:0;top:44px;width:273px;height:191px;filter:brightness(.7)"></div>
    <div class="a center" style="top:131px;font-family:Ubuntu,sans-serif;font-weight:700;font-size:15px;color:#fff">Out Of Stock</div>
    <div class="badge" style="top:180px"><i></i>30% OFF</div>
    <div class="a pname" style="left:14px;top:256px">Product Name</div>
    <div class="a" style="right:13px;top:252px;display:flex;align-items:baseline;gap:7px"><span class="price-old">$66.00</span><span class="price">$66.00</span></div>
    <div class="sizes" style="top:287px"><span>S</span><span>M</span><span>L</span><span>XL</span></div>
    <span class="swatch" style="left:14px;top:317px;background:#f06068"></span>
    <span class="swatch" style="left:37px;top:317px;background:#8fd6cc"></span>
    <span class="swatch" style="left:61px;top:317px;background:var(--slate)"></span>
    <div class="ship" style="top:319px"><svg width="11" height="9"><use href="#i-truck"/></svg>Free Shipping</div>
    <div class="tabs" style="top:364px"><span class="on">Description</span><span>Features</span><span>Shipping</span><span>Store Info</span><span>Returns</span></div>
    <p class="lorem" style="top:386px">Lorem ipsum odor amet, consectetuer adipiscing elit. Habitasse neque rhoncus lobortis vehicula hendrerit vel dapibus. Urna cursus facilisis senectus pulvinar neque laoreet venenatis. Ex feugiat felis fermentum laoreet class semper? Orci aliquam nulla mus sapien lorem porttitor venenatis nisi quisque. Eleifend elementum sem efficitur lobortis arcu. Turpis ridiculus vestibulum; faucibus adipiscing morbi at platea dictum.</p>
    <div class="pill" style="left:17px;top:548px;height:27px;width:156px">What size is the model wearing?</div>
    <div class="pill" style="left:185px;top:548px;height:27px;width:120px">How much is express shipping?</div>
    <div class="msg" style="left:17px;top:582px;height:35px"></div>
    <div class="send" style="left:225px;top:585px"><svg><use href="#i-arrow"/></svg></div>
    <div class="cta" style="left:0;background:var(--disabled);color:#9a9a9a">ADD TO CART</div>
    <div class="cta" style="left:137px;width:136px;background:var(--disabled);color:#9a9a9a;border-left:1px solid #b5b5b5">BUY NOW</div>
  </section>

  <!-- Cart -->
  <section class="screen" style="left:1162px;top:1227px;height:591px">
    <header class="topbar"><svg class="back"><use href="#i-back"/></svg><div class="brand">LoomBay</div><svg class="me"><use href="#i-user"/></svg></header>
    <div class="btn" style="left:38px;width:197px;top:62px"><svg width="13" height="13"><use href="#i-return"/></svg>CONTINUE SHOPPING</div>
    <div class="cart-card" style="top:110px;height:296px">
      <div class="cart-head">Rosa Lane</div>
      <div class="item-thumb photo" role="img" aria-label="Product thumbnail" style="top:60px"></div>
      <div class="item-name" style="top:58px">Product Name</div>
      <div class="item-meta" style="top:74px">Size: M<br>Color: Bone</div>
      <div class="remove" style="top:55px">×</div>
      <div class="stepper" style="top:98px"><b>−</b><span>1</span><b>+</b></div>
      <div class="item-price" style="top:102px">$66.00</div>
      <div class="rule" style="top:127px"></div>
      <div class="item-thumb photo" role="img" aria-label="Product thumbnail" style="top:142px"></div>
      <div class="item-name" style="top:142px">Product Name</div>
      <div class="item-meta" style="top:158px">Size: L<br>Color: True Navy</div>
      <div class="remove" style="top:139px">×</div>
      <div class="stepper" style="top:186px"><b>−</b><span>2</span><b>+</b></div>
      <div class="item-price" style="top:190px">$66.00</div>
      <div class="rule" style="top:227px"></div>
      <div class="a" style="left:7px;top:237px;font-size:9px;color:#333">Total</div>
      <div class="item-price" style="top:237px;font-size:9px">$132.00</div>
      <div class="rule" style="top:259px"></div>
      <div class="a center" style="top:271px;font-size:10.5px;font-weight:900;color:#222;display:flex;justify-content:center;gap:6px;align-items:center"><svg width="11" height="11"><use href="#i-cart"/></svg>CHECKOUT</div>
    </div>
    <div class="cart-card" style="top:426px;height:140px">
      <div class="cart-head">Rosa Lane</div>
      <div class="item-thumb photo" role="img" aria-label="Product thumbnail" style="top:60px"></div>
      <div class="item-name" style="top:58px">Product Name</div>
      <div class="item-meta" style="top:74px">Size: M<br>Color: Bone</div>
      <div class="remove" style="top:55px">×</div>
      <div class="stepper" style="top:98px"><b>−</b><span>1</span><b>+</b></div>
      <div class="item-price" style="top:102px">$66.00</div>
    </div>
    <nav class="tabbar">
      <div class="tab" style="left:52px"><svg><use href="#i-search"/></svg>Search</div>
      <div class="tab" style="left:136px"><svg><use href="#i-spark"/></svg>Recommendations</div>
      <div class="tab on" style="left:226px"><svg><use href="#i-cart"/></svg>Cart</div>
    </nav>
  </section>

  <!-- Recommendations -->
  <section class="screen" style="left:14px;top:1501px;height:592px">
    <header class="topbar"><div class="brand">LoomBay</div><svg class="me"><use href="#i-user"/></svg></header>
    <div class="a" role="img" aria-label="Promotional banner photo of a smiling young woman in warm golden tones" style="left:0;top:44px;width:273px;height:119px;background:linear-gradient(100deg,#7a5a2c 0%,#a07a3a 45%,#8f6a2f 100%)"></div>
    <div class="a center" style="top:75px;font-family:Ubuntu,sans-serif;font-weight:700;font-size:21px;line-height:25px;color:#fff">PROMOTE<br>HERE</div>
    <div class="a" style="left:120px;top:145px;display:flex;gap:4px"><i style="width:14px;height:6px;border-radius:3px;background:var(--orange)"></i><i style="width:6px;height:6px;border-radius:50%;background:#fff"></i><i style="width:6px;height:6px;border-radius:50%;background:#fff"></i></div>
    <div class="a pname" style="left:14px;top:178px;font-weight:500">20 Items</div>
    <div class="a" style="left:187px;top:179px;width:73px;height:18px;border:1px solid var(--orange);border-radius:9px;color:var(--orange);font-size:10px;display:flex;align-items:center;justify-content:center;gap:4px"><svg width="9" height="9"><use href="#i-sort"/></svg>Price</div>
    <div class="a small" style="left:14px;top:205px;display:flex;align-items:center;gap:8px"><span class="check"></span>Show free shipping only</div>
    <div class="a pname" style="left:14px;top:244px;font-weight:400">Direct Match</div>

    <article class="card" style="left:20px;top:272px;width:107px;height:170px">
      <div class="a center" style="top:6px;font-family:Ubuntu,sans-serif;font-weight:700;font-size:8.5px;color:#111">Rosa Lane</div>
      <div class="a photo" role="img" aria-label="Product photo" style="left:0;top:24px;width:107px;height:65px"></div>
      <div class="mini-badge" style="top:58px"><i></i>30% OFF</div>
      <div class="a" style="left:12px;top:98px;font-size:8.4px;color:#222">Product Name</div>
      <div class="a" style="left:12px;top:110px;font-size:5.5px;color:#888">Nearest Location</div>
      <div class="a" style="left:12px;top:124px;display:flex;gap:3px"><i style="width:7px;height:7px;border-radius:50%;border:1px solid #aaa"></i><i style="width:7px;height:7px;border-radius:50%;background:#222"></i><i style="width:7px;height:7px;border-radius:50%;background:#5aa7ee"></i><i style="width:7px;height:7px;border-radius:50%;background:#c9a27e"></i></div>
      <div class="a" style="right:6px;top:148px;display:flex;align-items:baseline;gap:3px"><span style="font-size:5.5px;color:#888;text-decoration:line-through">$66.00</span><span style="font-size:10px;font-weight:900;color:#111">$66.00</span></div>
    </article>
    <article class="card" style="left:146px;top:272px;width:107px;height:170px">
      <div class="a center" style="top:6px;font-family:Ubuntu,sans-serif;font-weight:700;font-size:8.5px;color:#111">Rosa Lane</div>
      <div class="a photo" role="img" aria-label="Product photo" style="left:0;top:24px;width:107px;height:65px"></div>
      <div class="mini-badge" style="top:58px"><i></i>30% OFF</div>
      <div class="a" style="left:12px;top:98px;font-size:8.4px;color:#222">Product Name</div>
      <div class="a" style="left:12px;top:110px;font-size:5.5px;color:#888">Nearest Location</div>
      <div class="a" style="left:12px;top:124px;display:flex;gap:3px"><i style="width:7px;height:7px;border-radius:50%;border:1px solid #aaa"></i><i style="width:7px;height:7px;border-radius:50%;background:#222"></i><i style="width:7px;height:7px;border-radius:50%;background:#5aa7ee"></i><i style="width:7px;height:7px;border-radius:50%;background:#c9a27e"></i></div>
      <div class="a" style="right:6px;top:148px;display:flex;align-items:baseline;gap:3px"><span style="font-size:5.5px;color:#888;text-decoration:line-through">$66.00</span><span style="font-size:10px;font-weight:900;color:#111">$66.00</span></div>
    </article>

    <nav class="tabbar">
      <div class="tab" style="left:52px"><svg><use href="#i-search"/></svg>Search</div>
      <div class="tab on" style="left:136px"><svg><use href="#i-spark"/></svg>Recommendations</div>
      <div class="tab" style="left:226px"><svg><use href="#i-cart"/></svg>Cart</div>
    </nav>
  </section>

</main>
</body>
</html>
```